CBD Boutique Business Card Needed

We are in need of a business card to reflect the direction of our latest products. We are a fully organic company in which our store and products are very heavy in wood and "natural" components. We decided to bring color into one of our brands and immediately knew this is where we needed to go.

We are NOT a cash grab CBD company. We could have done this wrong, slapped a label on a shit product and left it like that. I am passionate about sharing my experience with other veterans and opening a store and making it a comfortable place for others to come and see if they can have the same experience.

Target Market(s)

We are a dual market company. We do have a beauty line that will cover the costs of the majority of our business. But we also heavily cater to veterans and first responders. I am a veteran and this is how I found out about CBD. So the marketing needs to bring in our higher end beauty clientele but also be able to not put off our customers that readily need this.

Contact Information for Business Card

What we are looking for is a light, professional, boutique design that is is neither quite feminine or masculine. Attached is a picture of a store in Portland that we asked our store designer to get her inspiration from. But all natural wood and black outlines are what is mostly in there.

Attached are the following files:

Logo: An AI file with how we have our logo. I do not understand AI and have no idea why the letters are individual. The font is Adam. OLU is the logo and Tonics of Vigor is our tagline.

KM Vantage (front and back) cards I did originally found at a trade show that I absolutely loved...while it is mostly there and I would still be happy with them but it is me pretending to be you. I understand I am not and there is probably a lot wrong that all of you would see instantly and this is why I am here.

Dropper Bottle: This is our final product mock up

Water Color: I am semi flexible here. This water color is slightly different on every level of our brand. The color itself can change...we are not stuck on THIS particular one. If you happen to make a new one that is similar in style and we use it...then I will happily commission you to change the rest on our next product run. I am pretty sure you can use this statement as evidence later . =) .

But seriously, we heavily believe in pay it forward and will work with anyone here that may have a vision bigger than ours. The winner of this contest will get preferential consideration on our marketing materials (need letterhead etc. next, as well as a brochure, and website) so three more projects coming down the pipeline.

Information to use for your mockup is contained on the card images I have included. I would prefer CBD for wellness CBD for life to be more prominent. No where else on the card do we have CBD mentioned.

Font styles to use
Sans Serif

Colors

Designer to choose colors to be used in the design.

Requirements
Must have
• Double Sided
• Front: OLU logo on front of card will be raised embossed. Background is watercolor. One has been provided. Others are up for consideration. If the rest of your design is incredible and I don't like your watercolor I will just ask to swap it.
• Back: Standard information. Not stuck on anything here. I LOVE clean minimal designs. The bleed on the card I provided is a luxury...
• Font for title and OLU is Adam. Everything else I prefer san serif or as clean as possible.
Nice to have
• I Need to incorporate Naturally Nurturing somewhere on the card. Bold but not intrusive.

```html
<!DOCTYPE html>
<html lang="en">
<head>
<meta charset="UTF-8">
<title>OLU – Tonics of Vigor business card</title>
<link rel="stylesheet" href="https://fonts.googleapis.com/css2?family=Montserrat:wght@200;300;400;500&display=swap">
<style>
  :root {
    --page-bg: #e9e8e6;
    --card-white: #ffffff;
    --ink: #1a1a1a;
    --ink-soft: #333333;
    --accent-mauve: #b5718c;
    --wash-yellow: #f3ea7a;
    --wash-green: #c7e3a4;
    --wash-blue: #a9d9e6;
    --wash-pink: #eaa4b8;
    --wash-violet: #b9b3e0;
  }
  * { box-sizing: border-box; margin: 0; padding: 0; }
  html, body { width: 1200px; height: 900px; overflow: hidden; }
  body {
    background: var(--page-bg);
    font-family: "Montserrat", sans-serif;
    color: var(--ink);
    position: relative;
  }
  .card {
    position: absolute;
    top: 100px;
    width: 400px;
    height: 700px;
    border-radius: 28px;
    overflow: hidden;
    background: var(--card-white);
    box-shadow: 0 10px 30px rgba(0,0,0,0.18);
  }
  .card--info { left: 170px; }
  .card--brand { left: 630px; }

  /* watercolor areas */
  .watercolor-corner {
    position: absolute;
    right: -40px;
    top: 0;
    width: 300px;
    height: 520px;
    background:
      radial-gradient(ellipse 45% 35% at 65% 45%, rgba(234,164,184,0.75), transparent 70%),
      radial-gradient(ellipse 55% 40% at 70% 25%, rgba(169,217,230,0.7), transparent 70%),
      radial-gradient(ellipse 60% 45% at 60% 65%, rgba(243,234,122,0.8), transparent 72%);
    filter: blur(6px);
  }
  .watercolor-full {
    position: absolute;
    inset: 0;
    background:
      radial-gradient(ellipse 40% 25% at 45% 15%, rgba(234,164,184,0.8), transparent 70%),
      radial-gradient(ellipse 45% 30% at 70% 30%, rgba(185,179,224,0.75), transparent 70%),
      radial-gradient(ellipse 60% 30% at 75% 8%, rgba(243,234,122,0.9), transparent 70%),
      radial-gradient(ellipse 55% 35% at 85% 70%, rgba(243,234,122,0.6), transparent 72%),
      radial-gradient(ellipse 70% 45% at 35% 65%, rgba(169,217,230,0.9), transparent 75%),
      linear-gradient(160deg, var(--wash-yellow) 0%, var(--wash-green) 40%, var(--wash-blue) 75%, #eef7f4 100%);
  }

  /* info side */
  .brand-block {
    position: absolute;
    left: 56px;
    top: 190px;
  }
  .brand-name {
    font-weight: 200;
    font-size: 76px;
    letter-spacing: 8px;
    line-height: 1;
    color: var(--ink);
  }
  .brand-tagline {
    font-weight: 300;
    font-size: 15px;
    letter-spacing: 1.5px;
    text-transform: uppercase;
    margin-top: 8px;
    color: var(--ink);
  }
  .person {
    position: absolute;
    left: 56px;
    top: 350px;
  }
  .person-name {
    font-weight: 400;
    font-size: 18px;
    letter-spacing: 1px;
    text-transform: uppercase;
  }
  .person-title {
    font-weight: 400;
    font-size: 12px;
    letter-spacing: 1px;
    color: var(--accent-mauve);
    margin-top: 4px;
  }
  .address {
    position: absolute;
    left: 56px;
    top: 420px;
    font-size: 13px;
    line-height: 1.7;
    color: var(--ink-soft);
  }
  .contact-list {
    position: absolute;
    left: 56px;
    top: 490px;
    list-style: none;
    font-size: 13px;
    line-height: 1;
    color: var(--ink-soft);
  }
  .contact-list li {
    display: flex;
    align-items: center;
    gap: 10px;
    margin-bottom: 10px;
  }
  .contact-icon { width: 13px; height: 13px; fill: var(--accent-mauve); flex: none; }

  /* brand side */
  .frame {
    position: absolute;
    inset: 38px;
    border: 1.5px solid var(--ink);
  }
  .brand-center {
    position: absolute;
    left: 0; right: 0;
    top: 270px;
    text-align: center;
  }
  .brand-center .brand-name { font-size: 104px; letter-spacing: 12px; padding-left: 12px; }
  .brand-center .brand-tagline { font-size: 19px; letter-spacing: 2px; margin-top: 12px; }
</style>
</head>
<body>

  <section class="card card--info" aria-label="Card contact side">
    <div class="watercolor-corner" role="img" aria-label="Soft pastel watercolor wash in yellow, pink and blue"></div>

    <div class="brand-block">
      <div class="brand-name">OLU</div>
      <div class="brand-tagline">Tonics of Vigor</div>
    </div>

    <div class="person">
      <div class="person-name">Nadia Verhoeven</div>
      <div class="person-title">OWNER / CEO</div>
    </div>

    <address class="address" style="font-style:normal">
      4120 N Cedar Hollow Rd<br>
      Fairmont, OR 97401, Suite 200
    </address>

    <ul class="contact-list">
      <li>
        <svg class="contact-icon" viewBox="0 0 24 24" aria-hidden="true"><path d="M6.6 10.8a15 15 0 0 0 6.6 6.6l2.2-2.2a1 1 0 0 1 1-.25 11.4 11.4 0 0 0 3.6.6 1 1 0 0 1 1 1V20a1 1 0 0 1-1 1A17 17 0 0 1 3 4a1 1 0 0 1 1-1h3.5a1 1 0 0 1 1 1c0 1.25.2 2.45.6 3.6a1 1 0 0 1-.25 1z"/></svg>
        541.555.0148
      </li>
      <li>
        <svg class="contact-icon" viewBox="0 0 24 24" aria-hidden="true"><path d="M2 5h20v14H2z M3.5 6.5 12 13l8.5-6.5" fill-rule="evenodd"/><path d="M3 6l9 7 9-7" stroke="#fff" stroke-width="1.6" fill="none"/></svg>
        hello@olu.life
      </li>
      <li>
        <svg class="contact-icon" viewBox="0 0 24 24" aria-hidden="true"><circle cx="12" cy="12" r="10"/><path d="M2 12h20M12 2c3 3 3 17 0 20M12 2c-3 3-3 17 0 20" stroke="#fff" stroke-width="1.4" fill="none"/></svg>
        www.olu.life
      </li>
    </ul>
  </section>

  <section class="card card--brand" aria-label="Card brand side">
    <div class="watercolor-full" role="img" aria-label="Full-bleed pastel watercolor background in yellow, green, blue, pink and violet"></div>
    <div class="frame"></div>
    <div class="brand-center">
      <div class="brand-name">OLU</div>
      <div class="brand-tagline">Tonics of Vigor</div>
    </div>
  </section>

</body>
</html>
```